Construction Company Website Design

I need a Website Design for a Construction Company. I have attached logo and business card design files (a.i) to match styles and text for the website. I will need design for 3 pages:
1. A Home page
2. A secondary page (will be different information pages)
3. A contact page with submision form
Website to look professional and match the 'theme' across all pages, using main colours / reverse colours as per design files. Must be clear it is a construction related website without being over the top. Happy for the construction related details (whether that be images/outlines/backgrounds etc to be fairly subtle and not overbearing on the contect of the pages. It will be the content that will be most important, not the images within.

Content has not yet been fully completed but attached is a site map. Each page will need a space for the insertion of the relevant heading and associated content for that particular page. Example can be used as per attached map. If it is preferable to have content completed for this to be a more succesful project please advise and I will complete and submit.

Target Market(s)

Clients for potential construction projects. These could be a range of people. All would be very professional, well educated and put a substantial expection on the quality of website provided.

Industry/Entity Type

Construction

Number of Pages Required

3 page

Font styles to use
Serif
Sans Serif
Other font styles liked:
• fonts preferable as per design files provided unless designer beleives a different font would suit better

Requirements
Must have
• Colour scheme to match logo and business card files provided. Fonts that match as per provided files. Pages must be consistent with the theme carrying across all pages. All pages must have contact details at the bottom of the page.
• Contents of page 1 - 'Home page': multiple tab options / logo link
• Contents of page 2 - 'Secondary page': Top and side navigation / area for information and/or images.
• Contents of page - 'Contact us page': Top and side navigation / Submission form / area for logos such as linkdin, facebook etc.
Nice to have
• Would be good to have a or some generic construction related images - outlines / shadows / effects etc. These might be background images or outlines related to the relevant industry and are consistent across the pages. Could be outlines of buildings, images of men with hardhats etc etc. Good to see colour scheme as per design files used
Should not have
• No pictures of houses. Generally no photos. If any imagery of people must not show faces/details.

```html
<!DOCTYPE html>
<html lang="en">
<head>
<meta charset="utf-8">
<title>Kestrel Constructions</title>
<link rel="stylesheet" href="https://fonts.googleapis.com/css2?family=Exo+2:wght@500;600;700;800&family=Open+Sans:wght@400;600&display=swap">
<style>
  :root {
    --brand-blue: #1ba3e2;
    --ink-dark: #4f4f4f;
    --ink-body: #5e5e5e;
    --footer-bg: #585858;
    --footer-text: #e4e4e4;
    --footer-muted: #a9a9a9;
    --paper: #ffffff;
  }
  * { margin: 0; padding: 0; box-sizing: border-box; }
  html, body { width: 1200px; height: 584px; overflow: hidden; background: var(--paper); }
  body { font-family: "Open Sans", Arial, sans-serif; position: relative; }

  .hero {
    position: absolute; left: 0; top: 0; width: 1200px; height: 516px;
    background: linear-gradient(160deg, #eaf7fd 0%, #ffffff 35%, #ffffff 100%);
    overflow: hidden;
  }
  .hero-visual { position: absolute; left: 0; top: 0; width: 1200px; height: 516px; }

  .site-header {
    position: absolute; left: 0; top: 0; width: 1200px; height: 58px;
    background: rgba(255,255,255,0.55);
  }
  .brand {
    position: absolute; left: 210px; top: 11px; height: 36px;
    display: flex; align-items: center; gap: 10px; text-decoration: none;
  }
  .brand-square { width: 12px; height: 12px; background: var(--brand-blue); }
  .brand-name {
    font-family: "Exo 2", Arial, sans-serif; font-weight: 500;
    font-size: 16px; letter-spacing: 1.6px; color: var(--ink-dark); white-space: nowrap;
  }
  .main-nav {
    position: absolute; left: 553px; top: 23px;
    display: flex; gap: 17px; list-style: none;
  }
  .main-nav a {
    font-family: "Exo 2", Arial, sans-serif; font-weight: 500;
    font-size: 10.5px; letter-spacing: 1px; color: var(--ink-dark);
    text-decoration: none; display: block; padding-bottom: 5px; white-space: nowrap;
  }
  .main-nav a.is-active { border-bottom: 2px solid var(--brand-blue); }

  .hero-copy { position: absolute; left: 207px; top: 178px; width: 420px; }
  .hero-kicker {
    font-family: "Exo 2", Arial, sans-serif; font-weight: 800;
    font-size: 24px; letter-spacing: 1.5px; color: var(--brand-blue); line-height: 28px;
  }
  .hero-title {
    font-family: "Exo 2", Arial, sans-serif; font-weight: 700;
    font-size: 25px; letter-spacing: 1.8px; color: var(--ink-dark); line-height: 32px;
    white-space: nowrap;
  }
  .hero-text {
    margin-top: 22px; font-size: 12px; line-height: 17.5px; color: var(--ink-body); width: 300px;
  }
  .hero-button {
    display: inline-flex; align-items: center; gap: 6px;
    margin-top: 20px; height: 32px; width: 103px; padding: 0 6px;
    border: 1px solid var(--brand-blue); color: var(--ink-dark);
    font-family: "Exo 2", Arial, sans-serif; font-weight: 500;
    font-size: 10px; letter-spacing: 1px; text-decoration: none; white-space: nowrap;
  }

  .site-footer {
    position: absolute; left: 0; top: 516px; width: 1200px; height: 68px;
    background: var(--footer-bg);
  }
  .footer-nav {
    position: absolute; left: 210px; top: 29px; display: flex; gap: 14px; list-style: none;
  }
  .footer-nav a {
    font-family: "Exo 2", Arial, sans-serif; font-weight: 500; font-size: 9px; letter-spacing: 1px;
    color: var(--footer-text); text-decoration: none; white-space: nowrap;
  }
  .social-links { position: absolute; left: 650px; top: 24px; display: flex; gap: 6px; }
  .social-links a { width: 22px; height: 22px; background: #8a8a8a; display: block; }
  .footer-brand { position: absolute; left: 840px; top: 20px; }
  .footer-brand-name {
    font-family: "Exo 2", Arial, sans-serif; font-weight: 500;
    font-size: 10.5px; letter-spacing: 1.2px; color: var(--footer-text);
    display: flex; align-items: center; gap: 6px; white-space: nowrap;
  }
  .footer-brand-name::before { content: ""; width: 8px; height: 8px; background: var(--brand-blue); }
  .copyright { margin-top: 5px; font-size: 8.5px; color: var(--footer-muted); letter-spacing: 0.3px; white-space: nowrap; }
</style>
</head>
<body>
  <section class="hero">
    <svg class="hero-visual" viewBox="0 0 1200 516" role="img" aria-label="Photograph of a glass-facade tower rising diagonally across the right side of the hero">
      <defs>
        <linearGradient id="glassTone" x1="0" y1="1" x2="1" y2="0">
          <stop offset="0" stop-color="#7fb9dc"/>
          <stop offset="0.45" stop-color="#b7def2"/>
          <stop offset="0.8" stop-color="#d9eef8"/>
          <stop offset="1" stop-color="#9cc6df"/>
        </linearGradient>
        <linearGradient id="hazeTone" x1="0" y1="0" x2="1" y2="1">
          <stop offset="0" stop-color="#dff3fc"/>
          <stop offset="1" stop-color="#ffffff" stop-opacity="0"/>
        </linearGradient>
      </defs>
      <rect x="0" y="0" width="520" height="380" fill="url(#hazeTone)"/>
      <polygon points="355,516 560,250 700,110 860,20 930,0 1200,0 1200,516" fill="url(#glassTone)" opacity="0.9"/>
    </svg>

    <header class="site-header">
      <a class="brand" href="#" aria-label="Kestrel Constructions home">
        <span class="brand-square"></span>
        <span class="brand-name">KESTREL CONSTRUCTIONS</span>
      </a>
      <ul class="main-nav">
        <li><a class="is-active" href="#">HOME</a></li>
        <li><a href="#">ABOUT US</a></li>
        <li><a href="#">SERVICES</a></li>
        <li><a href="#">PROJECTS</a></li>
        <li><a href="#">CULTURE</a></li>
        <li><a href="#">NEWS</a></li>
        <li><a href="#">CONTACT US</a></li>
      </ul>
    </header>

    <div class="hero-copy">
      <p class="hero-kicker">WELCOME TO</p>
      <h1 class="hero-title">KESTREL CONSTRUCTION</h1>
      <p class="hero-text">Duis aute irure dolor in reprehenderit in voluptate velit esse cillum dolore&nbsp; eu fugiat nulla pariatur. Excepteur sint occae&shy;cat cupidatat</p>
      <a class="hero-button" href="#">EXPLORE MORE
        <svg width="14" height="8" viewBox="0 0 14 8" aria-hidden="true"><path d="M0 4H12M9 1L12 4L9 7" fill="none" stroke="#1ba3e2" stroke-width="1.2"/></svg>
      </a>
    </div>
  </section>

  <footer class="site-footer">
    <ul class="footer-nav">
      <li><a href="#">HOME</a></li>
      <li><a href="#">ABOUT US</a></li>
      <li><a href="#">SERVICES</a></li>
      <li><a href="#">PROJECTS</a></li>
      <li><a href="#">CULTURE</a></li>
      <li><a href="#">NEWS</a></li>
      <li><a href="#">CONTACT US</a></li>
    </ul>
    <div class="social-links">
      <a href="#" aria-label="Social profile one"></a>
      <a href="#" aria-label="Social profile two"></a>
      <a href="#" aria-label="Social profile three"></a>
    </div>
    <div class="footer-brand">
      <p class="footer-brand-name">KESTREL CONSTRUCTIONS</p>
      <p class="copyright">© copyright 2018 kestrel construction.</p>
    </div>
  </footer>
</body>
</html>
```